"Dario Quillon" Business Card

Friends

My name is "Dario Quillon" and I need your help! I need a new business card for my personal use.

As background, "Dario Quillon" is actually an alias that I use when I meet women. Please use your creative skills to create an amazing business card for me to use!

In addition to including my name and contact details (see the "Must Have" section), you may wish to add a catchphrase or a title if you think it would help me :)

For background, please see:

http://www.dailybrightwire.com/2013/07/23/morton-feld-dario-quillon_n_5129847.html

Looking forward to seeing what you can do for me.

Hugs and kisses,

Dario Quillon [courtesy of PixelHarbor]

Target Market(s)

Adult women in New York City...or anywhere really.

Industry/Entity Type

Business

Requirements
Must have
• Please include the following details:

Dario Quillon
P: +1-555-3QUILLN
E: secrets@darioquillon-mail.com
Nice to have
• You might include a catchphrase, like "Quillon is my surname But you can call me Mr Smoothstep".

Or perhaps a title, like "Dario Quillon, Head of Sexy Times".

You're creative...I will leave the details to you my friends.
Should not have
• Any references to my actual name...because then, what's the point in using an alias?

```html
<!DOCTYPE html>
<html lang="en">
<head>
<meta charset="utf-8">
<title>Dario Quillon – Business Card</title>
<link rel="stylesheet" href="https://fonts.googleapis.com/css2?family=Lato:wght@400&display=swap">
<style>
  :root {
    --card-bg: #302d28;
    --gold-dark: #8c7a2b;
    --gold-light: #c4a43a;
    --ink-light: #cbc7be;
    --ink-mid: #8e897f;
    --ink-dim: #625e56;
    --rule: #5b5750;
  }
  html, body {
    margin: 0;
    padding: 0;
    overflow: hidden;
    background: var(--card-bg);
  }
  .card {
    position: relative;
    width: 1200px;
    height: 776px;
    background: var(--card-bg);
    font-family: "Lato", "Gill Sans", sans-serif;
    overflow: hidden;
  }
  .speech-bubble {
    position: absolute;
    inset: 0;
  }
  .catchphrase {
    position: absolute;
    left: 272px;
    top: 158px;
    margin: 0;
    font-size: 43px;
    line-height: 70px;
    font-weight: 400;
    color: var(--ink-light);
  }
  .name {
    position: absolute;
    left: 272px;
    top: 300px;
    margin: 0;
    font-size: 30px;
    letter-spacing: 0.5em;
    font-weight: 400;
    color: var(--ink-mid);
  }
  .divider {
    position: absolute;
    left: 272px;
    top: 366px;
    width: 737px;
    height: 2px;
    background: var(--rule);
  }
  .contact {
    position: absolute;
    left: 272px;
    top: 396px;
    margin: 0;
    font-size: 30px;
    line-height: 54px;
    color: var(--ink-dim);
  }
</style>
</head>
<body>
<div class="card">
  <svg class="speech-bubble" width="1200" height="776" viewBox="0 0 1200 776" aria-hidden="true">
    <defs>
      <linearGradient id="goldStroke" x1="0" y1="1" x2="1" y2="0">
        <stop offset="0" stop-color="var(--gold-dark)"/>
        <stop offset="0.5" stop-color="var(--gold-light)"/>
        <stop offset="1" stop-color="var(--gold-dark)"/>
      </linearGradient>
    </defs>
    <path d="M150 116 H1086 V569 H240 L68 703 L150 540 Z"
          fill="none" stroke="url(#goldStroke)" stroke-width="18" stroke-linejoin="miter"/>
  </svg>

  <p class="catchphrase">Quillon is my surname,<br>But you can call me Mr Smoothstep</p>
  <h1 class="name">Dario Quillon</h1>
  <div class="divider"></div>
  <p class="contact">Tel: +1-555-3QUILLN<br>Email: secrets@darioquillon-mail.com</p>
</div>
</body>
</html>
```